Wix web design for healthcare IT consulting firm.

I am looking for a web design built in Wix that it will be easy for me to add or edit content in the future. The web site does not need to be overly complicated, but it should look very polished and professional. I also want to ensure it is mobile device friendly. I do not need any type of on-line purchasing ability. I will eventually do blogs, but for now it is a fairly standard web site with main page, about us, services provided, etc. I would also like a place for potential customers to contact us directly from the web site. I have included a Word document with some content for the web design. I have also included my logo and business card for reference. I would like to utilize similar colors as my business card. One of my primary competitors is https://vonmarlhq.example/

Target Market(s)

Target market could be nursing home CEO, CIO, or other leader at an organization that manages long term care facilities.

Number of Pages Required

5+ page

Colors
876aae

Requirements
Must have
• Be designed to be used in Wix. Use the content I provided to create and make web design. Allow to be viewed on mobile device. Please use similar color structure as attached business card. Please use attached logo in design.

```html
<!DOCTYPE html>
<html lang="en">
<head>
<meta charset="utf-8">
<title>Clearline Health Partners – Healthcare IT Consulting</title>
<link href="https://fonts.googleapis.com/css2?family=Open+Sans:wght@400;600;700&family=Poppins:wght@400;500;600&display=swap" rel="stylesheet">
<style>
:root{
  --purple:#6b4a9e;
  --purple-soft:#876aae;
  --purple-panel:rgba(135,106,174,.82);
  --dark:#2b2b2d;
  --topbar:#3a3a3c;
  --ink:#3d3d3d;
  --muted:#6a6a6a;
  --light:#f3f3f3;
  --white:#ffffff;
}
*{margin:0;padding:0;box-sizing:border-box}
html,body{width:1200px;height:3232px;overflow:hidden}
body{position:relative;font-family:"Open Sans",Arial,sans-serif;color:var(--ink);background:var(--white)}
.abs{position:absolute}
a{color:inherit;text-decoration:none}

/* top bar */
.top-bar{left:0;top:0;width:1200px;height:47px;background:var(--topbar);color:#ddd;font-size:11px;display:flex;justify-content:flex-end;align-items:center;padding-right:150px;gap:14px}
.top-bar b{color:#fff;font-weight:400;margin-left:4px}

/* utility row */
.utility-nav{top:71px;left:596px;display:flex;gap:22px;font-size:13px;color:#444;align-items:center;height:32px}
.btn-pill{background:var(--purple);color:#fff;border-radius:20px;display:flex;align-items:center;justify-content:center;font-family:"Poppins",sans-serif;font-size:13px}
.utility-donate{left:926px;top:71px;width:142px;height:33px}

/* main nav */
.main-nav{left:0;top:140px;width:1200px;height:58px;background:var(--purple)}
.brand{left:112px;top:133px;width:222px;height:72px;background:#fff;display:flex;align-items:center;justify-content:center;gap:8px}
.brand-name{font-family:"Open Sans",sans-serif;font-weight:700;font-size:19px;color:var(--purple)}
.brand-dot{width:14px;height:14px;border-radius:50%;background:var(--purple)}
.nav-links{left:526px;top:140px;height:58px;display:flex;align-items:center;gap:38px;color:#fff;font-size:14px}
.social-cells{left:962px;top:140px;height:58px;display:flex}
.social-cells span{width:54px;height:58px;border-left:1px solid rgba(255,255,255,.35);display:flex;align-items:center;justify-content:center}
.social-cells span:last-child{border-right:1px solid rgba(255,255,255,.35)}
.social-cells i{width:10px;height:10px;border-radius:50%;background:#fff}

/* hero */
.hero{left:0;top:198px;width:1200px;height:556px;background:linear-gradient(180deg,#5f93b3 0%,#8fb6c9 35%,#d9dde2 75%,#eef0f3 100%)}
.hero-title{left:0;top:258px;width:1200px;text-align:center;color:#fff;font-weight:700;font-size:26px;line-height:44px;text-transform:uppercase}
.hero-btn{left:474px;top:377px;width:252px;height:36px;font-size:13px}
.hero-wave{left:0;top:650px}

/* welcome */
.section-title{width:1200px;left:0;text-align:center;font-weight:700;font-size:22px;color:#4a4a4a;text-transform:uppercase}
.section-title em{font-style:normal;color:var(--purple)}
.divider{left:480px;width:240px;height:12px;display:flex;align-items:center;justify-content:center;gap:6px}
.divider::before,.divider::after{content:"";flex:1;height:1px;background:var(--purple-soft)}
.divider span{font-size:8px;font-weight:700;color:var(--purple)}
.welcome-text{left:162px;top:978px;width:876px;text-align:center;font-size:11px;line-height:22px;color:#555}

.service-card{top:1146px;width:233px;height:211px;background:#fff;box-shadow:0 2px 8px rgba(0,0,0,.1);text-align:center;padding:56px 16px 0}
.service-card h3{font-weight:400;font-size:16px;color:#444;line-height:22px;margin-bottom:10px}
.service-card p{font-size:11px;line-height:19px;color:#555}
.service-card svg{position:absolute;left:0;bottom:-10px}
.service-icon{width:78px;height:78px;border-radius:50%;background:var(--purple);border:4px solid #d8cce8;display:flex;align-items:center;justify-content:center}

/* EHR */
.ehr-photo{left:0;top:1458px;width:610px;height:433px;background:linear-gradient(135deg,#eef2f3 0%,#cfd9db 55%,#b9c4c6 100%)}
.ehr-panel{left:610px;top:1458px;width:590px;height:433px;background:var(--purple);color:#fff}
.ehr-title{left:670px;top:1518px;font-weight:700;font-size:20px;line-height:34px;text-transform:uppercase;color:#fff}
.ehr-tag{left:670px;top:1598px;font-size:9px;font-weight:700;color:#fff;border-bottom:1px solid #fff;padding-right:26px}
.ehr-list{list-style:none;font-size:10px;color:#fff;white-space:nowrap}
.ehr-list li{height:30px;display:flex;align-items:center;gap:7px}
.ehr-list li::before{content:"";width:10px;height:10px;border-radius:50%;background:#fff;flex:none}
.read-more{left:670px;top:1794px;width:142px;height:33px;background:#fff;color:var(--purple);font-size:13px;border-radius:20px;display:flex;align-items:center;justify-content:center;font-family:"Poppins",sans-serif}

/* contact */
.contact-box{left:299px;top:1930px;width:608px;height:418px;background:var(--light)}
.contact-title{left:299px;top:1972px;width:608px;text-align:center;font-size:22px;color:#444;font-weight:400}
.field{background:#fff;font-family:"Poppins",sans-serif;font-size:11px;color:#777;padding:0 14px;display:flex;align-items:center}
.field.msg{align-items:flex-start;padding-top:14px}
.submit{left:403px;top:2273px;width:394px;height:47px;background:var(--purple);color:#fff;font-family:"Poppins",sans-serif;font-size:14px;display:flex;align-items:center;justify-content:center}

/* map + hours */
.map{left:0;top:2417px;width:1200px;height:400px;background:linear-gradient(160deg,#eef0ef 0%,#e4e7e4 60%,#dfe5e0 100%)}
.map-pin{left:863px;top:2548px}
.hours{left:172px;top:2417px;width:246px;height:416px;background:var(--purple-panel);color:#fff;font-family:"Poppins",sans-serif;z-index:2}
.hours h4{font-size:14px;font-weight:600;text-align:center;margin-top:36px;text-transform:uppercase}
.hours .lead{font-size:11px;text-align:center;line-height:20px;margin:8px 30px 14px}
.hours-row{display:flex;font-size:10px;height:33px;align-items:center;padding-left:38px}
.hours-row b{width:76px;font-weight:600}
.hours h5{font-size:13px;font-weight:600;text-align:center;margin-top:10px;text-transform:uppercase}
.tab{left:172px;width:246px;height:36px;font-family:"Poppins",sans-serif;font-size:10px;font-weight:600;color:#fff;padding-left:56px;display:flex;align-items:center;z-index:3}
.tab-arrow{left:418px;top:2746px;z-index:3}

/* footer */
.footer{left:0;top:2740px;width:1200px;height:444px;z-index:1}
.foot-col{top:2986px;font-family:"Poppins",sans-serif;color:#fff;z-index:2}
.foot-col h4{font-size:15px;font-weight:400;margin-bottom:20px}
.foot-col p{font-size:11px;line-height:23px;color:#ddd}
.quick-links{display:grid;grid-template-columns:95px 90px;font-size:11px;line-height:23px;color:#ddd}
.foot-social{top:3110px;left:381px;display:flex;gap:12px;z-index:2}
.foot-social span{width:32px;height:32px;border:1px solid #999;border-radius:50%}
.foot-donate{left:862px;top:3121px;width:142px;height:33px;z-index:2}
.copyright{left:0;top:3184px;width:1200px;height:48px;background:#111;color:#bbb;font-size:11px;font-family:"Poppins",sans-serif;display:flex;align-items:center;justify-content:center;z-index:2}
</style>
</head>
<body>

<div class="abs top-bar"><span>email | <b>mreyes@clearlinehp.example</b></span><span>phone | <b>555-014-2290</b></span></div>

<nav class="abs utility-nav"><a>Insurance</a><a>Bill of Rights</a><a>Forms</a><a>Patient Portal</a></nav>
<a class="abs btn-pill utility-donate">Donate</a>

<div class="abs main-nav"></div>
<div class="abs brand"><span class="brand-dot"></span><span class="brand-name">Clearline</span></div>
<nav class="abs nav-links"><a>Home</a><a>About us</a><a>Service</a><a>Blog</a><a>Contact Us</a></nav>
<div class="abs social-cells"><span><i></i></span><span><i></i></span></div>

<div class="abs hero" role="img" aria-label="Photo of a smiling team of doctors and nurses in white coats"></div>
<h1 class="abs hero-title">Increasing the<br>value and security of your technology resources</h1>
<a class="abs btn-pill hero-btn">Schedule Your Next Appointment</a>
<svg class="abs hero-wave" width="1200" height="110" viewBox="0 0 1200 110">
  <path d="M0 40 C250 110 450 110 700 60 C900 20 1050 10 1200 30 L1200 110 L0 110Z" fill="#fff"/>
  <path d="M0 35 C250 105 450 105 700 55 C900 15 1050 5 1200 25" fill="none" stroke="var(--purple)" stroke-width="10"/>
  <path d="M0 62 C240 118 480 108 720 70" fill="none" stroke="var(--purple-soft)" stroke-width="3"/>
</svg>

<h2 class="abs section-title" style="top:880px">Welcome to <em>Healthcare IT Consulting Firm</em></h2>
<div class="abs divider" style="top:932px"><span>Clearline</span></div>
<p class="abs welcome-text">As the Founder and CEO of Clearline HP, Morgan has been working in the technology industry for over 25 years with extensive experience in healthcare and IT. As a consultant Morgan held multiple roles including CIO and CISO. Over the years, Morgan has been the executive sponsor of multiple electronic health record (EHR) implementations. He has created and nurtured numerous successful IT departments and created strong relationships with leadership teams. Morgan strives to learn and grow as a professional. He holds a Master's in Business Administration as well as a Master's in Healthcare Administration.</p>

<div class="abs service-card" style="left:215px">
  <h3>EHR Optimization Services</h3>
  <p>Provide guidance and resources to assist with improving the effective use of the customer's EHR system.</p>
  <svg width="233" height="20"><path d="M0 16 C70 2 150 2 233 12" stroke="var(--purple)" stroke-width="4" fill="none"/></svg>
</div>
<div class="abs service-card" style="left:474px">
  <h3>Policy Management and Consulting</h3>
  <p>Provide guidance on IT policy management, required and recommended by national Health Insurance Portability</p>
  <svg width="233" height="20"><path d="M0 16 C70 2 150 2 233 12" stroke="var(--purple)" stroke-width="4" fill="none"/></svg>
</div>
<div class="abs service-card" style="left:735px">
  <h3>Chief Information Officer</h3>
  <p>- Act as the organization's CIO or IT Director to assist with improving department's functions and effectiveness</p>
  <svg width="233" height="20"><path d="M0 16 C70 2 150 2 233 12" stroke="var(--purple)" stroke-width="4" fill="none"/></svg>
</div>
<div class="abs service-icon" style="left:292px;top:1108px"><svg width="34" height="34" viewBox="0 0 34 34" fill="none" stroke="#fff" stroke-width="2"><circle cx="17" cy="12" r="6"/><path d="M3 24 L12 24 L20 28 L31 22"/></svg></div>
<div class="abs service-icon" style="left:551px;top:1108px"><svg width="34" height="34" viewBox="0 0 34 34" fill="none" stroke="#fff" stroke-width="2"><rect x="8" y="4" width="18" height="26" rx="2"/><path d="M12 12h10M12 18h10M12 24h6"/></svg></div>
<div class="abs service-icon" style="left:812px;top:1108px"><svg width="34" height="34" viewBox="0 0 34 34" fill="none" stroke="#fff" stroke-width="2"><rect x="5" y="5" width="24" height="16" rx="2"/><circle cx="11" cy="26" r="4"/><circle cx="23" cy="26" r="4"/></svg></div>

<div class="abs ehr-photo" role="img" aria-label="Photo of a doctor caring for an elderly patient in a wheelchair"></div>
<div class="abs ehr-panel"></div>
<h2 class="abs ehr-title">Electronic Health Record<br>(EHR) Services</h2>
<span class="abs ehr-tag">Clearline</span>
<ul class="abs ehr-list" style="left:672px;top:1641px">
  <li>EHR Optimization Services the printing</li><li>EHR Implementation</li><li>EHR Assessment</li><li>EHR Quality Assessment</li>
</ul>
<ul class="abs ehr-list" style="left:884px;top:1641px">
  <li>On-Going EHR Support</li><li>Policy Management and Consulting</li><li>Chief Information Officer (CIO) Services</li><li>On-Going CIO or CISO Support</li>
</ul>
<a class="abs read-more">Read more</a>

<div class="abs contact-box"></div>
<h2 class="abs contact-title">CONTACT WITH US</h2>
<div class="abs divider" style="left:483px;top:2019px"><span>Clearline</span></div>
<div class="abs field" style="left:403px;top:2062px;width:192px;height:36px">Name</div>
<div class="abs field" style="left:607px;top:2062px;width:190px;height:36px">Email</div>
<div class="abs field" style="left:403px;top:2111px;width:192px;height:37px">Phone</div>
<div class="abs field" style="left:607px;top:2111px;width:190px;height:37px">Email</div>
<div class="abs field msg" style="left:403px;top:2158px;width:394px;height:95px">Message</div>
<a class="abs submit">Submit</a>

<div class="abs map" role="img" aria-label="Street map showing the office location"></div>
<svg class="abs map-pin" width="54" height="82" viewBox="0 0 54 82"><path d="M27 2 C12 2 2 13 2 27 C2 46 27 80 27 80 C27 80 52 46 52 27 C52 13 42 2 27 2Z" fill="var(--purple)"/><circle cx="27" cy="26" r="15" fill="#fff"/></svg>
<div class="abs hours">
  <h4>Working Hours</h4>
  <p class="lead">Lorem ipsum is simply dummy text of the printing</p>
  <div class="hours-row"><b>Monday</b>7:00am – 6:00pm</div>
  <div class="hours-row"><b>Tuesday</b>7:00am – 6:00pm</div>
  <div class="hours-row"><b>Wednesday</b>7:00am – 6:00pm</div>
  <div class="hours-row"><b>Thursday</b>7:00am – 6:00pm</div>
  <div class="hours-row"><b>Friday</b>7:00am – 4:00pm</div>
  <h5>Contact Details</h5>
</div>
<div class="abs tab" style="top:2737px;background:var(--purple)">Friday</div>
<svg class="abs tab-arrow" width="14" height="18"><path d="M0 0 L14 9 L0 18Z" fill="var(--purple)"/></svg>
<div class="abs tab" style="top:2773px;background:#5a4a74">Cedar Point</div>

<svg class="abs footer" width="1200" height="444" viewBox="0 0 1200 444">
  <path d="M0 80 C250 10 500 0 750 20 C950 35 1100 20 1200 0 L1200 444 L0 444Z" fill="var(--dark)"/>
  <path d="M30 150 C300 60 600 90 820 150 C940 180 1020 140 1070 130 C900 125 720 170 520 160 C330 150 180 110 30 150Z" fill="var(--purple)"/>
</svg>
<div class="abs foot-col" style="left:131px"><h4>Quick link</h4>
  <div class="quick-links"><span>Navigation</span><span>Locations</span><span>Services</span><span>Contact Us</span><span>Resources</span><span></span><span>About Us</span></div>
</div>
<div class="abs foot-col" style="left:381px"><h4>Address 1</h4><p>Alder Bay<br>27 Harbor Mill Rd<br>Alder Bay, MD 20990</p></div>
<div class="abs foot-col" style="left:614px"><h4>Address 2</h4><p>Cedar Point<br>418 Cedar Point Rd<br>Cedar Point, MD 20991</p></div>
<div class="abs foot-col" style="left:851px"><h4>Contact Us</h4><p>Alder Bay: 555-010-4700<br>Cedar Point: 555-010-2200<br>Behavioral Health: 555-016-1432</p></div>
<div class="abs foot-social"><span></span><span></span></div>
<a class="abs btn-pill foot-donate">Donate</a>
<div class="abs copyright">© 2018 All rights reserved</div>

</body>
</html>
```